Pitch Deck Powerpoint Template for Entrepreneurship/Education Based Nonprofit

I need a stylish powerpoint design for a start-up nonprofit called Bright Venture Works (BVW). I am building BVWs pitch deck to raise money. BVW is an entrepreneurial incubator and accelerator that seeks to identify, validate, test, and launch innovative ventures that improve public education. An example of our model, and one of our partners, is Nine Oaks Learning in New Orleans and New York :http://nineoakslearn.example

We need the deck to look sleek and innovative - like a start-up pitch deck. Lots of different templates and fonts that pop off the page.

Target Market(s)

Individuals, foundations, and any other stakeholder - we are pitching a new business model and asking for money.

Industry/Entity Type

Building

Font styles to use
Sans Serif

Requirements
Must have
• A sleek/modern feel with several different template slides. charts and graphs/ strong fonts that pop off the page, use of the logo:
• It would be great to have a slide describing the 3 primary programs at Bright Venture Works (BVW):
• - BVWspark - come in with an idea for an innovation in education, and we will do a two day workshop to examine your business assumptions and discuss next steps.
• - BVWpropel - take your idea to a prototype and launch to customers - we help you with an intensive 30 day program
• - BVWnurture - for existing nonprofit projects, we allow you to work under our umbrella to launch and build capacity
• Slides: Problem Definition, Solution, Value Proposition, Data/MEasurement, Key Partners, About the founder, Key Advisors

```html
<!DOCTYPE html>
<html lang="en">
<head>
<meta charset="utf-8">
<title>Primary Programs at BVW</title>
<link rel="stylesheet" href="https://fonts.googleapis.com/css2?family=Lato:wght@400;700;900&display=swap">
<style>
  :root {
    --navy: #1b3768;
    --plum: #8c1c6c;
    --ink: #1d1d1f;
    --paper: #ffffff;
    --bullet-edge: #6a7fa6;
  }
  * { margin: 0; padding: 0; box-sizing: border-box; }
  html, body {
    width: 1200px;
    height: 675px;
    overflow: hidden;
    background: var(--paper);
  }
  .slide {
    position: relative;
    width: 1200px;
    height: 675px;
    background: var(--paper);
    font-family: "Lato", Arial, sans-serif;
    color: var(--ink);
  }
  .slide-title {
    position: absolute;
    left: 94px;
    top: 38px;
    font-size: 63px;
    font-weight: 700;
    color: var(--navy);
    letter-spacing: -0.3px;
    line-height: 1.2;
  }
  .rule-accent {
    position: absolute;
    left: 0;
    top: 151px;
    width: 70px;
    height: 11px;
    background: var(--plum);
  }
  .rule-main {
    position: absolute;
    left: 75px;
    top: 145px;
    width: 1125px;
    height: 23px;
    background: var(--navy);
  }
  .program-list {
    position: absolute;
    left: 94px;
    top: 200px;
    list-style: none;
  }
  .program {
    position: relative;
    padding-left: 39px;
    width: 470px;
    font-size: 33px;
    line-height: 1.21;
    color: var(--ink);
  }
  .program::before {
    content: "";
    position: absolute;
    left: 0;
    top: 13px;
    width: 13px;
    height: 13px;
    border: 1.5px solid var(--bullet-edge);
  }
  .program-name { font-weight: 700; }
  .brand-name {
    position: absolute;
    left: 818px;
    top: 512px;
    font-size: 50px;
    font-weight: 900;
    line-height: 0.98;
    color: var(--navy);
    letter-spacing: -0.5px;
  }
</style>
</head>
<body>
  <main class="slide">
    <h1 class="slide-title">Primary Programs at BVW</h1>
    <div class="rule-accent"></div>
    <div class="rule-main"></div>
    <ul class="program-list">
      <li class="program"><span class="program-name">BVWnurture</span> – For existing nonprofit projects, we allow you to work under our umbrella to launch and build capacity.</li>
    </ul>
    <div class="brand-name">Bright<br>Venture<br>Works</div>
  </main>
</body>
</html>
```